Modern Irish Pub. We need to find "our look" for new bar.

We have a logo, color scheme and feel of what we want but we need someone to work with to create flyer designs, menu, website and social content.

Young vibrant mixed with traditional Irish. Think neon & sexy mixed with wood and traditional Irish.

Looking for examples of social media posts and flyers. We can then hire for more work! We need to find “our look”.
Updates

Low design quality

Target Market(s)

21-40 year olds

Industry/Entity Type

Bar and Restaurant.

Colors
EB3D1F
EC4F4E
F09395
F8D3D4
FCEDEE

Requirements
Must have
• Our logo.
Nice to have
• Young mixed with traditional. Sexy l, vibrant and fun.
Should not have
• Cartoon like child like look and feel.

```html
<!DOCTYPE html>
<html lang="en">
<head>
<meta charset="utf-8">
<title>Scarlet Harp Irish Pub – Social &amp; Flyer Set</title>
<link href="https://fonts.googleapis.com/css2?family=Alfa+Slab+One&family=Anton&family=Great+Vibes&family=Libre+Baskerville:wght@400;700&family=Sorts+Mill+Goudy&display=swap" rel="stylesheet">
<style>
:root{
  --red:#EB3D1F;
  --tag:#E8202A;
  --coral:#EC4F4E;
  --pink:#F09395;
  --blush:#F8D3D4;
  --cream:#FCEDEE;
  --ink:#000;
  --white:#fff;
  --amber:#e89a2a;
  --wood:#5a2e12;
  --neon-violet:#5a2aa0;
  --neon-magenta:#a0287a;
}
*{margin:0;padding:0;box-sizing:border-box}
html,body{width:1200px;height:972px;overflow:hidden}
body{
  background:radial-gradient(ellipse 60% 55% at 50% 52%,#5a0b10 0%,#33060a 45%,#0b0203 85%,#000 100%);
  position:relative;font-family:"Libre Baskerville",serif;color:var(--white);
}
.tile{position:absolute;overflow:hidden}
.photo{position:absolute;inset:0}
.brand{
  position:absolute;display:flex;align-items:center;gap:4px;
  font-family:"Libre Baskerville",serif;font-weight:700;color:var(--white);
  text-transform:uppercase;line-height:1.05;text-align:center;
}
.brand .dot{width:7px;height:7px;border-radius:50%;background:var(--red);flex:none}
.brand.small{font-size:6.5px}
.tag{
  position:absolute;background:var(--tag);color:var(--white);
  font-family:"Libre Baskerville",serif;font-weight:700;white-space:nowrap;
}
.tag.small{font-size:7px;padding:3px 5px}

/* left column */
.t-cheers{left:65px;top:53px;width:241px;height:241px}
.t-cheers .photo{background:
  radial-gradient(ellipse 30% 18% at 60% 35%,rgba(240,170,60,.75) 0%,transparent 70%),
  radial-gradient(ellipse 22% 20% at 18% 22%,rgba(190,140,110,.55) 0%,transparent 70%),
  radial-gradient(ellipse 22% 20% at 40% 18%,rgba(200,150,115,.5) 0%,transparent 70%),
  radial-gradient(ellipse 22% 20% at 80% 20%,rgba(200,150,115,.5) 0%,transparent 70%),
  radial-gradient(ellipse 25% 12% at 50% 4%,rgba(255,200,120,.45) 0%,transparent 70%),
  radial-gradient(ellipse 45% 35% at 100% 100%,rgba(90,40,200,.85) 0%,transparent 75%),
  radial-gradient(ellipse 45% 35% at 0% 100%,rgba(150,30,50,.8) 0%,transparent 75%),
  linear-gradient(180deg,#3a2a22 0%,#2a1c18 40%,#3a1436 72%,#241050 100%)}
.t-cheers h2{position:absolute;left:0;right:0;top:138px;text-align:center;font-family:"Libre Baskerville",serif;font-weight:400;font-size:26px;line-height:27px}
.t-cheers .tag{left:78px;top:202px}
.t-cheers .brand{left:0;right:0;top:102px;justify-content:center}

.t-calm{left:65px;top:311px;width:241px;height:240px}
.t-calm .photo{background:
  radial-gradient(ellipse 22% 16% at 18% 80%,rgba(200,100,30,.8) 0%,transparent 70%),
  radial-gradient(ellipse 18% 22% at 24% 40%,rgba(230,160,50,.6) 0%,transparent 70%),
  radial-gradient(ellipse 14% 18% at 60% 12%,rgba(230,170,70,.5) 0%,transparent 70%),
  radial-gradient(ellipse 16% 20% at 88% 40%,rgba(220,150,50,.45) 0%,transparent 70%),
  radial-gradient(ellipse 60% 50% at 30% 55%,#6a3a10 0%,#3a1e0a 50%,transparent 90%),
  linear-gradient(180deg,#1a0e06 0%,#120803 70%,#060302 100%)}
.t-calm h2{position:absolute;left:95px;top:106px;width:130px;text-align:center;font-family:"Anton",sans-serif;font-style:italic;font-weight:400;font-size:23px;line-height:24px;letter-spacing:1px}
.t-calm .brand{left:180px;top:24px}

.t-match{left:65px;top:568px;width:241px;height:240px}
.t-match .photo{background:
  radial-gradient(ellipse 14% 18% at 73% 60%,rgba(220,140,50,.7) 0%,transparent 70%),
  radial-gradient(ellipse 14% 18% at 90% 58%,rgba(220,140,50,.6) 0%,transparent 70%),
  radial-gradient(ellipse 24% 22% at 38% 22%,rgba(180,130,100,.45) 0%,transparent 70%),
  radial-gradient(ellipse 24% 22% at 68% 18%,rgba(180,130,100,.4) 0%,transparent 70%),
  radial-gradient(ellipse 40% 25% at 55% 0%,rgba(150,80,50,.55) 0%,transparent 70%),
  linear-gradient(180deg,#4a3a2c 0%,#33281f 45%,#18110c 75%,#0a0705 100%)}
.t-match .script{position:absolute;left:44px;top:136px;font-family:"Great Vibes",cursive;font-size:40px;line-height:1}
.t-match .bold{position:absolute;left:84px;top:169px;font-family:"Anton",sans-serif;font-style:italic;font-size:31px;line-height:1;letter-spacing:1px}
.t-match .brand{left:10px;top:210px}
.t-match .note{position:absolute;right:12px;top:213px;font-size:6.6px;font-weight:700;text-align:right;line-height:8px}

/* centre flyer */
.flyer{left:335px;top:53px;width:511px;height:755px;background:var(--ink)}
.flyer .photo{top:310px;background:
  radial-gradient(ellipse 20% 14% at 20% 52%,rgba(255,240,220,.55) 0%,transparent 70%),
  radial-gradient(ellipse 14% 9% at 48% 7%,rgba(255,240,220,.4) 0%,transparent 70%),
  radial-gradient(ellipse 22% 32% at 20% 78%,rgba(255,170,40,.9) 0%,rgba(220,120,20,.5) 45%,transparent 75%),
  radial-gradient(ellipse 12% 40% at 48% 45%,rgba(240,150,40,.85) 0%,transparent 75%),
  radial-gradient(ellipse 22% 30% at 80% 50%,rgba(250,170,50,.75) 0%,transparent 75%),
  radial-gradient(ellipse 30% 25% at 92% 85%,rgba(170,110,50,.6) 0%,transparent 75%),
  radial-gradient(ellipse 30% 28% at 10% 20%,rgba(120,70,30,.6) 0%,transparent 75%),
  linear-gradient(180deg,#000 0%,#2a1606 10%,#5a3010 35%,#7a4410 65%,#3a200a 100%)}
.flyer .brand{left:0;right:0;top:48px;justify-content:center;font-size:15px}
.flyer .rule{position:absolute;left:55px;width:400px;height:1px;background:var(--white)}
.flyer h1{position:absolute;left:0;right:0;top:128px;text-align:center;font-family:"Alfa Slab One",serif;font-weight:400;font-size:53px;letter-spacing:.5px;line-height:1}
.flyer .sub{position:absolute;left:55px;width:400px;top:194px;height:44px;display:flex;justify-content:space-between;align-items:center;font-family:"Libre Baskerville",serif;font-weight:700;font-size:35px}
.flyer .sub i{width:10px;height:10px;border-radius:50%;background:var(--white)}
.flyer .lead{position:absolute;left:46px;right:46px;top:272px;text-align:center;font-family:"Sorts Mill Goudy",serif;font-size:15px;line-height:21px}
.flyer .panel{position:absolute;left:211px;top:375px;width:300px;height:227px;background:rgba(0,0,0,.55)}
.flyer .panel p{position:absolute;right:40px;top:14px;text-align:right;font-family:"Sorts Mill Goudy",serif;font-size:15px;line-height:21px;white-space:nowrap}
.flyer .tag{left:290px;top:551px;width:181px;height:30px;font-size:17px;text-align:center;line-height:30px;font-family:"Sorts Mill Goudy",serif;letter-spacing:.5px}

/* right column */
.t-dia{left:884px;top:46px;width:248px;height:248px}
.t-dia .photo{background:
  radial-gradient(ellipse 18% 28% at 50% 38%,rgba(235,90,70,.85) 0%,transparent 70%),
  radial-gradient(ellipse 14% 10% at 18% 72%,rgba(240,190,110,.7) 0%,transparent 70%),
  radial-gradient(ellipse 14% 10% at 84% 66%,rgba(240,180,90,.7) 0%,transparent 70%),
  radial-gradient(ellipse 40% 12% at 50% 78%,rgba(140,80,30,.55) 0%,transparent 75%),
  radial-gradient(ellipse 12% 12% at 44% 10%,rgba(200,190,210,.45) 0%,transparent 70%),
  radial-gradient(ellipse 45% 40% at 10% 30%,rgba(110,50,170,.7) 0%,transparent 75%),
  radial-gradient(ellipse 40% 40% at 95% 35%,rgba(90,50,140,.6) 0%,transparent 75%),
  linear-gradient(180deg,#2a1a3c 0%,#1e1224 60%,#0c080c 100%)}
.t-dia .bar{position:absolute;left:11px;top:17px;width:8px;height:29px;background:var(--tag)}
.t-dia h2{position:absolute;left:27px;top:15px;font-family:"Libre Baskerville",serif;font-weight:400;font-size:16px;line-height:18px}
.t-dia .brand{left:188px;top:22px}

.t-uair{left:884px;top:307px;width:248px;height:248px}
.t-uair .photo{background:
  radial-gradient(ellipse 14% 16% at 30% 42%,rgba(230,180,150,.55) 0%,transparent 70%),
  radial-gradient(ellipse 14% 16% at 55% 40%,rgba(220,160,140,.5) 0%,transparent 70%),
  radial-gradient(ellipse 14% 16% at 78% 44%,rgba(220,160,140,.5) 0%,transparent 70%),
  radial-gradient(ellipse 40% 40% at 0% 0%,rgba(240,60,30,.9) 0%,transparent 75%),
  radial-gradient(ellipse 40% 40% at 100% 100%,rgba(70,30,110,.8) 0%,transparent 75%),
  linear-gradient(120deg,#c8281c 0%,#7a1a2a 45%,#3a1030 80%,#241030 100%)}
.t-uair h2{position:absolute;left:51px;top:138px;font-family:"Libre Baskerville",serif;font-weight:700;font-size:26px;line-height:27px}
.t-uair h2 span{display:block;padding-left:40px}
.t-uair .note{position:absolute;left:45px;top:198px;font-size:5.6px;font-weight:700;line-height:8px}
.t-uair .tag{right:9px;top:229px}
.t-uair .brand{left:188px;top:22px}

.t-rock{left:884px;top:567px;width:248px;height:248px}
.t-rock .photo{background:
  radial-gradient(circle at 78% 22%,rgba(255,255,255,.8) 0%,rgba(255,255,255,0) 5%),
  radial-gradient(ellipse 12% 14% at 10% 24%,rgba(220,160,130,.55) 0%,transparent 70%),
  radial-gradient(ellipse 12% 14% at 34% 28%,rgba(210,150,120,.5) 0%,transparent 70%),
  radial-gradient(ellipse 12% 14% at 58% 30%,rgba(170,110,90,.5) 0%,transparent 70%),
  radial-gradient(ellipse 12% 14% at 92% 24%,rgba(210,150,120,.5) 0%,transparent 70%),
  radial-gradient(ellipse 12% 14% at 72% 40%,rgba(210,150,120,.45) 0%,transparent 70%),
  radial-gradient(ellipse 10% 12% at 50% 56%,rgba(220,150,50,.55) 0%,transparent 70%),
  radial-gradient(ellipse 50% 30% at 50% 12%,rgba(120,50,180,.7) 0%,transparent 75%),
  linear-gradient(180deg,#2a1a3a 0%,#3a2030 35%,#2a1812 65%,#0a0606 100%)}
.t-rock .brand{left:100px;top:22px}
.t-rock .line{position:absolute;line-height:1;transform:rotate(-9deg);transform-origin:left bottom}
.t-rock .l1{left:38px;top:150px;color:var(--white);font-family:"Anton",sans-serif;font-size:36px;letter-spacing:1px}
.t-rock .l2{left:44px;top:186px;color:var(--tag);font-family:"Libre Baskerville",serif;font-weight:700;font-size:27px}
.t-rock .tag{right:6px;top:229px}
</style>
</head>
<body>

<section class="tile t-cheers">
  <div class="photo" role="img" aria-label="Friends laughing and clinking beer glasses at a neon-lit bar"></div>
  <div class="brand small"><span class="dot"></span><span>Scarlet<br>Harp</span></div>
  <h2>DRINK &amp;<br>CHEERS</h2>
  <div class="tag small">4.20 pm to 12.00am</div>
</section>

<section class="tile t-calm">
  <div class="photo" role="img" aria-label="Warm wooden pub interior with barrel and whisky signs"></div>
  <div class="brand small"><span class="dot"></span><span>Scarlet<br>Harp</span></div>
  <h2>KEEP<br>CALM<br>DRINK<br>BEER</h2>
</section>

<section class="tile t-match">
  <div class="photo" role="img" aria-label="Two friends toasting beer mugs at a pub table"></div>
  <div class="script">Friendly</div>
  <div class="bold">MATCH</div>
  <div class="brand small"><span class="dot"></span><span>Scarlet<br>Harp</span></div>
  <p class="note">Lorem ipsum dolor sit amet,<br>consectetur adipiscing elit sed.</p>
</section>

<section class="tile flyer">
  <div class="photo" role="img" aria-label="Glasses of golden beer with foam, a wooden barrel and wheat on a table"></div>
  <div class="brand"><span class="dot"></span><span>Scarlet<br>Harp</span></div>
  <div class="rule" style="top:122px"></div>
  <h1>HAPPY HOUR</h1>
  <div class="sub"><i></i><span>J</span><span>U</span><span>N</span><span>C</span><span>T</span><span>I</span><span>O</span><span>N</span><i></i></div>
  <div class="rule" style="top:242px"></div>
  <p class="lead">Lorem ipsum dolor sit amet, consectetur adipiscing elit, sed<br>do eiusmod tempor incididunt ut labore et dolore magna<br>aliqua. Quis ipsum suspendisse ultrices gravida. Risus com-<br>modo viverra maecenas accumsan lacus vel facilisis.</p>
  <div class="panel">
    <p>Lorem ipsum dolor sit amet,<br>consectetur adipiscing elit, sed do<br>eiusmod tempor incididunt ut labore<br>et dolore magna aliqua. Quis ipsum<br>suspendisse ultrices gravida. Risus<br>commodo viverra maecenas<br>accumsan lacus vel facilisis.</p>
  </div>
  <div class="tag">4.20 pm to 12.00am</div>
</section>

<section class="tile t-dia">
  <div class="photo" role="img" aria-label="Server carrying beer tasting flights in a dim purple bar"></div>
  <div class="bar"></div>
  <h2>DIA NA<br>CARRAIGEACHA!</h2>
  <div class="brand small"><span class="dot"></span><span>Scarlet<br>Harp</span></div>
</section>

<section class="tile t-uair">
  <div class="photo" role="img" aria-label="Young women dancing at a party under red light"></div>
  <div class="brand small"><span class="dot"></span><span>Scarlet<br>Harp</span></div>
  <h2>UAIR AN<span>БTHAIS</span></h2>
  <p class="note">Lorem ipsum dolor sit amet, consectetur adipiscing elit,<br>sed do eiusmod tempor incididunt ut labore et dolore<br>magna aliqua. Quis ipsum suspendisse ultrices gravida.</p>
  <div class="tag small">4.20 pm to 12.00am</div>
</section>

<section class="tile t-rock">
  <div class="photo" role="img" aria-label="Group of friends cheering with beers in a neon bar"></div>
  <div class="brand small"><span class="dot"></span><span>Scarlet<br>Harp</span></div>
  <div class="line l1">ROCK</div>
  <div class="line l2">YOUR LIFE!</div>
  <div class="tag small">4.20 pm to 12.00am</div>
</section>

</body>
</html>
```